Business Card for Quillmark Ledger - A cannabis publication for executives.

I'd like some business cards for Quillmark Ledger. The logo is done (great job!) and I need a card design I will use with PRINTLY. I made it a short project to allow time for printing before an event. These will be standard sized cards (final artwork size 3.66" x 2.16" at 300dpi) with a final card size of 3.5" x 2.0". (See PRINTLY.com if you need more info.) I might try rounded corners but am not sure yet. I think the design will work okay with rounded.

Quillmark Ledger will be a bi-weekly publication for the cannabis industry. It is targeted to investors and industry executives, not consumers or pot smokers. So our market is more B2B. However I am open to creativity and making the card something people remark on.

My contact for card:

Dana Merrow
Founder/CEO
dana@quillmarkledger.example

2740 Harlow Avenue
Boston MA 02135
(617)555-0194

Target Market(s)

Executives, Industry people and investors in the Cannabis sector.

Contact Information for Business Card

PRINTLY does do double sided and the second side can be the same or different images. Only one side is required but use of the second side would be a bonus.

Font styles to use
Serif
Sans Serif
Decorative

Colors

Designer to choose colors to be used in the design.

Requirements
Must have
• Logo, contact info
Nice to have
• Style and design to make the card stand out in a crowd.

```html
<!DOCTYPE html>
<html lang="en">
<head>
<meta charset="utf-8">
<title>Quillmark Ledger — Business Card</title>
<link rel="stylesheet" href="https://fonts.googleapis.com/css2?family=EB+Garamond:wght@700&family=Open+Sans:wght@400&display=swap">
<style>
  :root {
    --backdrop: #82928f;
    --paper: #ffffff;
    --brand-blue: #0f76bd;
    --brand-green: #80ad33;
    --ink-light: #ffffff;
  }
  * { box-sizing: border-box; margin: 0; padding: 0; }
  html, body {
    width: 1200px; height: 1000px; overflow: hidden;
    background: var(--backdrop);
  }
  .card {
    position: absolute; left: 80px; top: 133px;
    width: 1040px; height: 695px;
    border-radius: 40px; overflow: hidden;
    background: var(--paper);
  }
  .card-shapes { position: absolute; inset: 0; }
  .brand {
    position: absolute; left: 102px; top: 170px;
    display: flex; align-items: center; gap: 22px;
  }
  .brand-square {
    width: 62px; height: 62px; background: var(--brand-green);
  }
  .brand-name {
    font-family: "EB Garamond", Georgia, serif;
    font-weight: 700; font-size: 58px; line-height: 1;
    color: var(--brand-blue);
  }
  .person {
    position: absolute; left: 720px; top: 245px;
    color: var(--ink-light);
  }
  .person-name {
    font-family: "EB Garamond", Georgia, serif;
    font-weight: 700; font-size: 50px; line-height: 1;
  }
  .person-title {
    font-family: "Open Sans", Arial, sans-serif;
    font-size: 21px; margin-top: 10px;
  }
  .contact-row {
    position: absolute; left: 54px; top: 527px;
    display: flex; align-items: center; gap: 34px;
    font-family: "Open Sans", Arial, sans-serif;
    font-size: 22px; color: var(--ink-light);
  }
  .contact-item { display: flex; align-items: center; gap: 12px; }
  .contact-icon {
    width: 54px; height: 54px; border-radius: 50%;
    background: var(--paper);
    display: flex; align-items: center; justify-content: center;
    flex: none;
  }
  .contact-address { text-align: center; line-height: 1.35; }
</style>
</head>
<body>
  <div class="card">
    <svg class="card-shapes" width="1040" height="695" viewBox="0 0 1040 695">
      <rect x="0" y="450" width="1040" height="245" fill="var(--brand-blue)"/>
      <path d="M388,450 C600,380 780,250 742,0 L1040,0 L1040,450 Z" fill="var(--brand-green)"/>
      <path d="M388,450 C600,380 780,250 742,0" fill="none" stroke="var(--brand-blue)" stroke-width="6"/>
    </svg>

    <div class="brand">
      <div class="brand-square"></div>
      <div class="brand-name">Quillmark Ledger</div>
    </div>

    <div class="person">
      <div class="person-name">Dana Merrow</div>
      <div class="person-title">Founder/CEO</div>
    </div>

    <div class="contact-row">
      <div class="contact-item">
        <span class="contact-icon">
          <svg width="28" height="28" viewBox="0 0 24 24"><path fill="var(--brand-blue)" d="M6.6 10.8c1.4 2.8 3.8 5.1 6.6 6.6l2.2-2.2c.3-.3.7-.4 1-.2 1.1.4 2.3.6 3.6.6.6 0 1 .4 1 1V20c0 .6-.4 1-1 1C10.6 21 3 13.4 3 4c0-.6.4-1 1-1h3.5c.6 0 1 .4 1 1 0 1.3.2 2.5.6 3.6.1.3 0 .7-.2 1z"/></svg>
        </span>
        <span>(617)555-0194</span>
      </div>
      <div class="contact-item">
        <span class="contact-icon">
          <svg width="32" height="24" viewBox="0 0 32 24"><rect x="2" y="3" width="28" height="18" fill="none" stroke="var(--brand-blue)" stroke-width="2"/><path d="M2 3 L16 14 L30 3 M2 21 L12 11 M30 21 L20 11" fill="none" stroke="var(--brand-blue)" stroke-width="2"/></svg>
        </span>
        <span>dana@quillmarkledger.example</span>
      </div>
      <div class="contact-item">
        <span class="contact-icon">
          <svg width="22" height="30" viewBox="0 0 22 30"><path fill="var(--brand-blue)" d="M11 0C5 0 0 5 0 11c0 8 11 19 11 19s11-11 11-19C22 5 17 0 11 0zm0 16a5 5 0 1 1 0-10 5 5 0 0 1 0 10z"/></svg>
        </span>
        <span class="contact-address">2740 Harlow Avenue<br>Boston MA 02135</span>
      </div>
    </div>
  </div>
</body>
</html>
```